Realtor / Kitchen & Bath Designer / Curb Appeal Specialist Before & After Postcard

Realtor / Curb Appeal Specialist / Kitchen & Bath Designer / Interior Decorator / Real Estate Staging

I need an oversized postcard to send to luxury / waterfront homes and condominiums. I have a background photo and 3 sets of Before and After photos and a professional photo for my bio which I would like to be on the back with room for address labels and postage.

I offer a FREE (No obligation) in-home design / staging consultation for potential homeowners interesed in selling their home or condominium. I will place some of these cards in open houses, related businesses, some will be direct mailed, some will be handed out.

My goal with this marketing is to attract potential SELLERS who realize that they need my skills, ideas, experience for: Curb Appeal / Facade Enhancement / landscaping ... Kitchen & Bath Updating ... Decorating / Paint Colors ... Staging, etc ... in order to help SELL their properties FASTER and with HIGHER NET PROCEEDS on the real estate market ... and HOPEFULLY LISTING their property with me as their Listing Realtor.

I realize this is a bit complicated but I hopfully the photos will mostly convey the message ... with text as needed, more elegantly than I have worded this. Here are some POINTS that I am trying to make:

Curb Appeal, Landscaping, Updated Kitchens & Baths, Paint Colors, Lighting ... are more important than ever ... to sell upscale waterfront homes/condominiums in this competitive market ... design savvy BUYERS are looking for quality fixtures, features, and WOW factors.

Bio. Brennic Dwale is a Florida Realtor and licensed Interior Decorator, Kitchen & Bath Designer, and Curb Appeal Specialist with 25+ years experience in the residential design/remodeling industry.

Photos are: Professional photo (can be cropped and/or B/W with Bio on back) ... Photos are in order: 6 sets of Before - After, with addtional photo.

Target Market(s)

Home and Condo owners who are wanting to SELL their home and hopefully LIST with me as a REALTOR. I also pick up some design work.

Industry/Entity Type

Landscaping

Requirements
Must have
• Front: The entire front could be a faded - muted (half tone) photo of the kitchen (last photo) ... then 3 or 4 sets of smaller before & after pics with borders. The after photos could be slightly larger than the before pics which could be inset or superimposed/offset at the bottom. There should be a lead line at the top such as :

"Serious about selling your home or condominium?" and maybe at the bottom: "Today's design savvy BUYERS desire updated kitchens and baths, quality fixtures, design features, and attractive landscaping."

Back: My bio with photo. Room for hand written or address labels/postage. Perhaps the Before & After of the condo bathroom could also be on the back at the left /top with my photo/bio smaller at the left bottom.
Nice to have
• somehow make it seem classy and elegant ... not like a sales pitch
Should not have
• anything that looks or sounds tacky.

```html
<!DOCTYPE html>
<html lang="en">
<head>
<meta charset="utf-8">
<title>Brennic Dwale – Before &amp; After Postcard</title>
<link rel="stylesheet" href="https://fonts.googleapis.com/css2?family=Arimo:wght@400;700&family=EB+Garamond:ital,wght@1,400;1,500&family=Roboto+Condensed:wght@400;700&display=swap">
<style>
  :root {
    --navy: #34434f;
    --tan: #b39a78;
    --beige: #ddd2c4;
    --ink: #2f3a44;
    --paper: #ffffff;
    --backdrop: #ecebe8;
    --serif: "EB Garamond", Georgia, serif;
    --cond: "Roboto Condensed", "Arial Narrow", sans-serif;
    --sans: "Arimo", Arial, sans-serif;
  }
  * { margin: 0; padding: 0; box-sizing: border-box; }
  html, body { width: 1200px; height: 960px; overflow: hidden; }
  body { background: var(--backdrop); position: relative; font-family: var(--sans); color: var(--ink); }

  .card {
    position: absolute;
    left: 312px;
    width: 543px;
    height: 422px;
    background: var(--paper);
    transform: scale(1.06);
    transform-origin: top left;
    overflow: hidden;
  }
  .card--front { top: 18px; }
  .card--back { top: 495px; }

  .photo { position: absolute; }
  .label-tag {
    position: absolute; left: 8px; bottom: 3px;
    font: 700 7px var(--sans); color: #fff; letter-spacing: .3px;
  }
  .band { position: absolute; }
  .band--navy { background: var(--navy); }
  .band--tan { background: var(--tan); }

  /* Front */
  .front-hero {
    left: 0; top: 0; width: 380px; height: 330px;
    background: linear-gradient(180deg, #d8d1c6 0%, #8f877c 35%, #3b3835 65%, #1f1f1f 100%);
  }
  .front-before {
    left: 384px; top: 0; width: 159px; height: 88px;
    background: linear-gradient(180deg, #c9dbe4 0%, #8fc2bc 45%, #7ea06a 100%);
  }
  .front-after {
    left: 384px; top: 103px; width: 159px; height: 85px;
    background: linear-gradient(180deg, #cfdce2 0%, #e9ecec 45%, #7f9c63 100%);
  }
  .front-question {
    position: absolute; left: 384px; top: 205px; width: 159px; height: 125px;
    background: var(--beige);
    display: flex; align-items: center;
    padding: 0 18px;
    font: italic 400 17px/1.15 var(--serif); color: var(--navy);
  }
  .front-name { position: absolute; left: 62px; top: 305px; font-family: var(--cond); }
  .front-name .first { display: block; font-size: 26px; font-weight: 400; color: #fff; letter-spacing: .5px; line-height: 1; }
  .front-name .last { display: block; font-size: 21px; font-weight: 700; color: var(--navy); letter-spacing: .5px; line-height: 1.2; margin-top: 2px; }
  .front-title {
    position: absolute; left: 62px; top: 362px; width: 90px;
    font: italic 400 8px/1.3 var(--sans); color: var(--ink);
  }
  .front-phone { position: absolute; left: 62px; top: 396px; font: 700 9.5px var(--sans); color: var(--navy); }
  .front-pitch {
    position: absolute; left: 240px; top: 362px; width: 272px;
    font: 400 12.5px/1.35 var(--sans); color: var(--ink);
  }
  .front-pitch strong { font-weight: 700; }

  /* Back */
  .back-facade-before {
    left: 0; top: 0; width: 158px; height: 88px;
    background: linear-gradient(180deg, #b8b2a4 0%, #a49d8e 55%, #8c877c 100%);
  }
  .back-facade-after {
    left: 164px; top: 0; width: 158px; height: 88px;
    background: linear-gradient(135deg, #c9c6bd 0%, #6e726a 50%, #5f8f3f 100%);
  }
  .back-headline {
    position: absolute; left: 33px; top: 116px; width: 300px;
    font: italic 400 15px/1.2 var(--serif); color: var(--navy);
  }
  .back-body {
    position: absolute; left: 33px; top: 161px; width: 290px;
    font: 400 9.3px/1.3 var(--sans); color: var(--ink);
  }
  .back-offer-title {
    position: absolute; left: 38px; top: 219px;
    font: 700 13px/1 var(--cond); color: var(--navy); letter-spacing: .3px;
  }
  .offer-list {
    position: absolute; left: 30px; top: 238px; width: 291px; height: 57px;
    background: var(--navy);
    list-style: none;
    display: grid; grid-template-columns: 146px 1fr; column-gap: 10px;
    padding: 9px 10px 0;
  }
  .offer-list li {
    font: 700 7.4px var(--sans); color: #fff;
    padding: 4px 0 5px;
    white-space: nowrap;
  }
  .offer-list li:nth-child(-n+2) { border-bottom: 1px solid #6b7984; }
  .portrait {
    left: 30px; top: 318px; width: 56px; height: 74px;
    background: linear-gradient(180deg, #8a7a62 0%, #4e4538 50%, #1f2a3a 100%);
  }
  .back-name { position: absolute; left: 96px; top: 320px; font-family: var(--cond); }
  .back-name .first { display: block; font-size: 22px; font-weight: 400; color: var(--tan); letter-spacing: .3px; line-height: 1; }
  .back-name .last { display: block; font-size: 19px; font-weight: 700; color: var(--navy); letter-spacing: .5px; line-height: 1.2; }
  .back-phone { position: absolute; left: 96px; top: 374px; font: 700 9.5px var(--sans); color: var(--navy); }
  .bio-rule { position: absolute; left: 190px; top: 318px; width: 1px; height: 74px; background: #c9c9c9; }
  .bio {
    position: absolute; left: 203px; top: 320px; width: 104px;
    font: italic 400 7.4px/1.3 var(--sans); color: var(--ink);
  }
  .bio strong { font-weight: 700; }
</style>
</head>
<body>

<section class="card card--front" aria-label="Postcard front">
  <div class="photo front-hero" role="img" aria-label="Staged living room with dark tiled fireplace, black leather sofa and French doors"></div>

  <div class="photo front-before" role="img" aria-label="Before: small teal cottage with overgrown lawn">
    <span class="label-tag">BEFORE</span>
  </div>
  <div class="band band--navy" style="left:384px; top:90px; width:159px; height:8px;"></div>
  <div class="photo front-after" role="img" aria-label="After: renovated white cottage with landscaped yard">
    <span class="label-tag">AFTER</span>
  </div>
  <div class="band band--tan" style="left:384px; top:191px; width:159px; height:9px;"></div>
  <p class="front-question">Want to capitalize on your property’s true potential?</p>

  <h2 class="front-name"><span class="first">BRENNIC</span><span class="last">DWALE</span></h2>
  <p class="front-title">Florida Realtor and Licensed Interior Decorator.</p>
  <p class="front-phone">Phone number</p>

  <p class="front-pitch">Today’s design savvy <strong>BUYERS</strong> desire updated kitchens and baths, quality fixtures, design features, and attractive landscaping.</p>
</section>

<section class="card card--back" aria-label="Postcard back">
  <div class="photo back-facade-before" role="img" aria-label="Before: stone home front with garage door"></div>
  <div class="band band--navy" style="left:0; top:91px; width:158px; height:9px;"></div>
  <div class="photo back-facade-after" role="img" aria-label="After: home entry with pergola and tropical planting"></div>
  <div class="band band--tan" style="left:164px; top:91px; width:158px; height:9px;"></div>

  <p class="back-headline">It is paramount that a buyer’s first impression of your home inspires a vision of their desired lifestyle.</p>
  <p class="back-body">Leave design decisions to me and experience interiors with a difference. International research shows that staged homes sell faster, maximising price potential. I have over 25 years experience in the residential design/remodeling industry.</p>

  <h3 class="back-offer-title">I OFFER EXPERIENCE IN:</h3>
  <ul class="offer-list">
    <li>Curb appeal</li>
    <li>Kitchen and bathroom design</li>
    <li>Facade enhancement / landscaping</li>
    <li>Color consultancy</li>
  </ul>

  <div class="photo portrait" role="img" aria-label="Professional portrait of the realtor in a dark suit"></div>
  <h2 class="back-name"><span class="first">BRENNIC</span><span class="last">DWALE</span></h2>
  <p class="back-phone">Phone number</p>
  <div class="bio-rule"></div>
  <p class="bio"><strong>Brennic Dwale</strong> is a Florida Realtor and licensed interior decorator, kitchen &amp; bath designer, and curb appeal specialist with 25+ years experience in the residential design/remodeling industry.</p>
</section>

</body>
</html>
```